Summer Time Cleaning!

Breeze Haven Partners Inc. is a family owned business since 2007, QRVTL certified techs, using the most advanced equipment offered in the field. Would like to attract as many customers as possible to bring in a swarm of work during our slow time.please print on jumbo size post card.

Target Market(s)

Main line area homes worth $500,000+

Industry/Entity Type

Residential

Requirements
Must have
• Would like special on Air duct cleaning: Air Duct Cleaning Special- Full home power air duct cleaning only $300.00 offer expires August 29th. Dryer Vent Cleaning Special- Any dryer vent cleaning services includes a FREE lint alert system!
Nice to have
• Would like bright colors, need the post card to really stand out!

```html
<!DOCTYPE html>
<html lang="en">
<head>
<meta charset="utf-8">
<title>Breeze Haven Partners – Summer Air Duct Cleaning Postcard</title>
<link rel="stylesheet" href="https://fonts.googleapis.com/css2?family=Bebas+Neue&family=Oswald:wght@700&display=swap">
<style>
  :root {
    --wall-light: #d9cfc0;
    --wall-mid: #b7a992;
    --wall-dark: #8a7c68;
    --floor-light: #c79a63;
    --floor-dark: #8e6437;
    --sky-pale: #d4f1fb;
    --sky-light: #8fd6f2;
    --ocean: #2a9ad6;
    --ocean-deep: #1678b8;
    --brand-teal: #3fc3cc;
    --accent-yellow: #ffd21f;
    --ink-white: #ffffff;
    --ink-dark: #1b1b1b;
    --badge-blue: #2c3f9e;
    --text-shade: rgba(40, 30, 20, 0.55);
  }
  * { margin: 0; padding: 0; box-sizing: border-box; }
  html, body { width: 1200px; height: 662px; overflow: hidden; background: #ffffff; }
  .postcard {
    position: relative;
    width: 1200px;
    height: 662px;
    overflow: hidden;
    font-family: "Bebas Neue", "Oswald", sans-serif;
  }
  .room-photo {
    position: absolute;
    inset: 0;
    background:
      linear-gradient(180deg, transparent 0%, transparent 68%, var(--floor-light) 68%, var(--floor-dark) 100%),
      radial-gradient(ellipse at 45% 35%, var(--wall-light) 0%, var(--wall-mid) 60%, var(--wall-dark) 100%);
  }
  .brand-name {
    position: absolute;
    left: 172px;
    top: 48px;
    width: 560px;
    font-family: "Oswald", "Arial Narrow", sans-serif;
    font-weight: 700;
    font-size: 78px;
    line-height: 86px;
    color: var(--brand-teal);
  }
  .pitch {
    position: absolute;
    left: 258px;
    top: 258px;
    font-size: 39px;
    line-height: 41px;
    letter-spacing: 0.3px;
    text-transform: uppercase;
    color: var(--ink-white);
    text-shadow: 1px 1px 2px var(--text-shade);
  }
  .pitch .highlight { color: var(--accent-yellow); }
  .specials {
    position: absolute;
    right: 28px;
    top: 40px;
    width: 360px;
    text-align: right;
    text-transform: uppercase;
    color: var(--ink-white);
    text-shadow: 1px 1px 3px var(--text-shade);
  }
  .special + .special { margin-top: 16px; }
  .special-title {
    font-size: 36px;
    line-height: 38px;
    color: var(--accent-yellow);
  }
  .special-detail {
    font-size: 26px;
    line-height: 29px;
  }
  .special-price { color: var(--accent-yellow); }
  .wave-band {
    position: absolute;
    left: 0;
    top: 0;
    width: 1200px;
    height: 662px;
  }
  .before-after {
    position: absolute;
    left: 36px;
    top: 418px;
    width: 228px;
    height: 228px;
    border-radius: 50%;
    border: 10px solid var(--sky-light);
    background: radial-gradient(circle at 50% 40%, #e9e9e9 0%, #9a9a9a 55%, #3e3e3e 100%);
    overflow: hidden;
  }
  .before-after-labels {
    position: absolute;
    left: 0;
    bottom: 50px;
    width: 100%;
    text-align: center;
    font-size: 28px;
    letter-spacing: 0.5px;
  }
  .before-after-labels .before { color: var(--ink-dark); }
  .before-after-labels .after { color: var(--ink-white); }
  .cert-badge {
    position: absolute;
    left: 252px;
    top: 436px;
    width: 186px;
    height: 186px;
    border-radius: 50%;
    background: var(--ink-white);
    border: 10px solid var(--sky-light);
    box-shadow: inset 0 0 0 16px #ffffff, inset 0 0 0 22px var(--badge-blue);
  }
  .call-line {
    position: absolute;
    left: 478px;
    top: 594px;
    font-size: 46px;
    line-height: 1;
    color: var(--accent-yellow);
    white-space: nowrap;
  }
  .phone {
    position: absolute;
    left: 930px;
    top: 594px;
    display: flex;
    align-items: center;
    gap: 8px;
    font-size: 46px;
    line-height: 1;
    color: var(--ink-white);
    white-space: nowrap;
  }
  .phone svg { width: 28px; height: 28px; margin-top: -4px; }
</style>
</head>
<body>
<main class="postcard">
  <div class="room-photo" role="img" aria-label="Photo of a baby sitting on a wooden floor in front of a dirty, moldy wall air vent"></div>

  <h1 class="brand-name">Breeze Haven Partners</h1>

  <section class="specials" aria-label="Summer specials">
    <div class="special">
      <p class="special-title">Air Duct Cleaning Special</p>
      <p class="special-detail">Full home power air duct cleaning<br>only <span class="special-price">$300.00</span></p>
      <p class="special-detail">Offer expires August 29th</p>
    </div>
    <div class="special">
      <p class="special-title">Dryer Vent Cleaning Special</p>
      <p class="special-detail">Any dryer vent cleaning service includes<br>a <span class="special-price">FREE</span> lint alert system!</p>
    </div>
  </section>

  <p class="pitch">
    Dont waste your money on cheap<br>
    imitators using impoper methods<br>
    <span class="highlight">Our methods are not only affordable<br>
    but done right the first time!</span>
  </p>

  <svg class="wave-band" viewBox="0 0 1200 662" aria-hidden="true">
    <path d="M0 470 C 260 395, 520 470, 760 520 C 930 555, 1080 560, 1200 545 L1200 662 L0 662 Z" fill="var(--sky-pale)"/>
    <path d="M0 500 C 260 440, 520 510, 760 548 C 930 575, 1080 580, 1200 565 L1200 662 L0 662 Z" fill="var(--sky-light)"/>
    <path d="M0 530 C 260 480, 520 545, 760 572 C 930 590, 1080 590, 1200 580 L1200 662 L0 662 Z" fill="var(--ocean)"/>
    <path d="M0 600 C 400 575, 800 600, 1200 585 L1200 662 L0 662 Z" fill="var(--ocean-deep)" opacity="0.55"/>
  </svg>

  <div class="before-after" role="img" aria-label="Before and after photo of the inside of an air duct">
    <div class="before-after-labels"><span class="before">BEFORE</span> <span class="after">AFTER</span></div>
  </div>

  <div class="cert-badge" aria-hidden="true"></div>

  <p class="call-line">CALL FOR A FREE ESTIMATE</p>
  <p class="phone">
    <svg viewBox="0 0 24 24" aria-hidden="true">
      <circle cx="12" cy="12" r="11" fill="none" stroke="#ffffff" stroke-width="2"/>
      <path d="M8.2 6.5c.4-.3 1-.2 1.3.2l1.2 1.8c.3.4.2 1-.2 1.3l-.8.6c.6 1.4 1.6 2.5 3 3.2l.6-.8c.3-.4.9-.5 1.3-.2l1.8 1.2c.4.3.5.9.2 1.3l-.8 1c-.5.6-1.4.8-2.1.5-3-1.3-5.3-3.6-6.5-6.6-.3-.7-.1-1.6.5-2.1z" fill="#ffffff"/>
    </svg>
    215-555-0148
  </p>
</main>
</body>
</html>
```